I need business cards for a company that will be an umbrella for many retail stores. I need them to be sleek and modern. I would like some white and black in the background of the card as these are the office colours the logo is attached.
Target Market(s)
worldwide
Industry/Entity Type
Business
Requirements
Must have
- traditional business card shape
Should not have
- too many colours
no swirly text

```html
<!DOCTYPE html>
<html lang="en">
<head>
<meta charset="utf-8">
<title>Navio Trading — Business Cards</title>
<link rel="stylesheet" href="https://fonts.googleapis.com/css2?family=Open+Sans:wght@400;600&display=swap">
<style>
  :root {
    --backdrop: #d8c99e;
    --card-white: #ffffff;
    --card-border: #e6e1d3;
    --brand-blue: #0b5ea8;
    --ink: #1a1a1a;
    --ink-soft: #333333;
    --icon-grey: #8a8f96;
    --on-blue: #ffffff;
  }
  * { box-sizing: border-box; margin: 0; padding: 0; }
  html, body {
    width: 1200px; height: 900px; overflow: hidden;
    font-family: "Open Sans", Arial, sans-serif;
  }
  .stage {
    position: relative; width: 1200px; height: 900px;
    background: var(--backdrop);
  }
  .card {
    position: absolute;
    background: var(--card-white);
    border: 4px solid var(--card-border);
  }

  /* Front card */
  .card--front { left: 36px; top: 8px; width: 768px; height: 426px; }
  .card--front .divider {
    position: absolute; left: 358px; top: 36px; width: 3px; height: 350px;
    background: var(--brand-blue);
  }
  .contact-block {
    position: absolute; right: 418px; text-align: right; color: var(--ink);
  }
  .contact-block .person-name { font-size: 25px; line-height: 1.2; }
  .contact-block .person-email { font-size: 18px; color: var(--ink-soft); margin-top: 6px; }
  .card--front .identity { top: 86px; }
  .contact-line {
    position: absolute; display: flex; align-items: center; gap: 14px;
    font-size: 18px; color: var(--ink-soft);
  }
  .contact-line svg { width: 28px; height: 28px; fill: var(--icon-grey); }
  .card--front .contact-line { right: 418px; }
  .card--front .line-phone { top: 240px; }
  .card--front .line-address { top: 282px; }

  .brand {
    position: absolute; display: flex; align-items: center; gap: 16px;
    color: var(--brand-blue); font-weight: 400; white-space: nowrap;
  }
  .brand .brand-dot {
    width: 34px; height: 34px; border-radius: 50%; background: var(--brand-blue);
  }
  .card--front .brand { left: 390px; top: 188px; font-size: 38px; letter-spacing: 1px; }

  /* Back card */
  .card--back { left: 396px; top: 466px; width: 716px; height: 430px; }
  .blue-panel {
    position: absolute; left: 194px; top: 0; width: 486px; height: 100%;
    background: var(--brand-blue); color: var(--on-blue);
  }
  .blue-panel .identity { position: absolute; left: 38px; top: 112px; }
  .blue-panel .person-name { font-size: 25px; line-height: 1.2; }
  .blue-panel .person-email { font-size: 18px; margin-top: 6px; }
  .blue-panel .contact-line { right: 36px; color: var(--on-blue); }
  .blue-panel .contact-line svg { fill: var(--on-blue); }
  .blue-panel .line-phone { top: 238px; }
  .blue-panel .line-address { top: 278px; }

  .card--back .brand {
    left: 97px; top: 215px; font-size: 32px; letter-spacing: 1px;
    transform: translate(-50%, -50%) rotate(-90deg);
  }
  .card--back .brand .brand-dot { width: 28px; height: 28px; }
</style>
</head>
<body>
<main class="stage" role="img" aria-label="Beige backdrop with white polka dots presenting the cards">

  <section class="card card--front">
    <div class="contact-block identity">
      <p class="person-name">Your name</p>
      <p class="person-email">email@yourdomain.com</p>
    </div>
    <p class="contact-line line-phone">Your telephone
      <svg viewBox="0 0 24 24" aria-hidden="true"><path d="M16 2h3l1 5-3 1.5c-.8 3 .2 6.5 2.4 8.8L17 20l1 2h-3C10 18 9 8 16 2z"/></svg>
    </p>
    <p class="contact-line line-address">Your Address
      <svg viewBox="0 0 24 24" aria-hidden="true"><path d="M2 21h20v2H2zM3 9h18v2H3zM12 1l10 6H2zM5 12h2v8H5zm4 0h2v8H9zm4 0h2v8h-2zm4 0h2v8h-2z"/></svg>
    </p>
    <div class="divider"></div>
    <p class="brand"><span class="brand-dot"></span>Navio Trading</p>
  </section>

  <section class="card card--back">
    <p class="brand"><span class="brand-dot"></span>Navio Trading</p>
    <div class="blue-panel">
      <div class="identity">
        <p class="person-name">Your name</p>
        <p class="person-email">email@yourdomain.com</p>
      </div>
      <p class="contact-line line-phone">Your telephone
        <svg viewBox="0 0 24 24" aria-hidden="true"><path d="M16 2h3l1 5-3 1.5c-.8 3 .2 6.5 2.4 8.8L17 20l1 2h-3C10 18 9 8 16 2z"/></svg>
      </p>
      <p class="contact-line line-address">Your Address
        <svg viewBox="0 0 24 24" aria-hidden="true"><path d="M2 21h20v2H2zM3 9h18v2H3zM12 1l10 6H2zM5 12h2v8H5zm4 0h2v8H9zm4 0h2v8h-2zm4 0h2v8h-2z"/></svg>
      </p>
    </div>
  </section>

</main>
</body>
</html>
```